Gather the Marrow Book Cover

Looking for a cover for my book, Gather the Marrow. Part memoir, part self help - this book is one woman's journey breaking free of the patriarchy and stepping into her divine purpose. Think "boss ass bitch" in NYC transitions to Spiritual Goddess to the beaches of Costa Rica. We are playing on the archetypes of Wounded Masculine to Divine Feminine. Breaking the mold of being a good girl and owning her wild.

Target Market(s)

25-35 yr old female

Industry/Entity Type

Personal Development, Memoir

Other font styles liked:
• Pink #ff0099 Yellow #ffdf2b Teal #1fc4cd Gather - Brittany The - open sans Marrow - Bebas Neue

Colors
FFF300
FFF600
FEFA6F
FFFEC7
FFFEE8
E54698
E96AAD
F1A4CE
F9D9EA
FCEFF6

Requirements
Nice to have

```html
<!DOCTYPE html>
<html lang="en">
<head>
<meta charset="utf-8">
<title>Gather the Marrow – Book Cover</title>
<link rel="stylesheet" href="https://fonts.googleapis.com/css2?family=Allura&family=Crimson+Text&family=Roboto+Condensed:wght@700&display=swap">
<style>
  :root{
    --paper:#ededed;
    --wash:#f6bcd3;
    --wash-soft:#f9d9ea;
    --magenta:#e6007e;
    --leaf:#ea6aa3;
    --leaf-deep:#d9457f;
    --yellow:#f9ec1f;
  }
  html,body{margin:0;padding:0;width:816px;height:1200px;overflow:hidden;background:var(--paper);}
  .cover{
    position:relative;width:816px;height:1200px;overflow:hidden;
    background:
      radial-gradient(ellipse 520px 420px at 120px 260px, var(--wash) 0%, rgba(249,217,234,.7) 55%, rgba(237,237,237,0) 100%),
      radial-gradient(ellipse 520px 480px at 720px 1080px, #f3a9c7 0%, rgba(246,188,211,.75) 45%, rgba(237,237,237,0) 100%),
      radial-gradient(ellipse 260px 360px at 790px 620px, var(--wash-soft) 0%, rgba(237,237,237,0) 100%),
      var(--paper);
  }
  .art{position:absolute;border-radius:50%;}
  .art--leaves-top-left{left:-10px;top:-10px;width:300px;height:250px;
    background:radial-gradient(ellipse at 45% 40%, var(--leaf) 0%, rgba(234,106,163,.45) 50%, rgba(234,106,163,0) 75%);}
  .art--leaves-top-right{left:655px;top:10px;width:160px;height:140px;
    background:radial-gradient(ellipse at 55% 45%, rgba(234,106,163,.7) 0%, rgba(234,106,163,.25) 50%, rgba(234,106,163,0) 75%);}
  .art--flowers-bottom-left{left:-20px;top:880px;width:530px;height:330px;
    background:radial-gradient(ellipse at 40% 65%, #f2a3c4 0%, rgba(234,106,163,.55) 45%, rgba(234,106,163,0) 75%);}
  .overline{position:absolute;left:0;width:816px;top:58px;text-align:center;
    font:400 42px/1 "Crimson Text",serif;color:var(--magenta);letter-spacing:1px;}
  .title-script{position:absolute;left:40px;width:730px;top:215px;text-align:center;
    font:400 250px/1 "Allura",cursive;color:var(--magenta);}
  .title-joiner{position:absolute;left:505px;top:452px;
    font:400 64px/1 "Crimson Text",serif;color:var(--magenta);}
  .title-main{position:absolute;left:0;width:816px;top:548px;text-align:center;
    font:700 190px/1 "Roboto Condensed",sans-serif;color:var(--yellow);
    text-shadow:4px 6px 8px rgba(70,60,20,.55);letter-spacing:2px;}
  .author{position:absolute;right:50px;top:920px;text-align:right;
    font:400 92px/0.98 "Crimson Text",serif;color:var(--magenta);}
</style>
</head>
<body>
  <main class="cover">
    <div class="art art--leaves-top-left" role="img" aria-label="Watercolour pink leaves on a branch"></div>
    <div class="art art--leaves-top-right" role="img" aria-label="Watercolour pink leaf sprig"></div>
    <div class="art art--flowers-bottom-left" role="img" aria-label="Watercolour pink blossoms and leafy stems"></div>

    <p class="overline" style="margin:0">A Memoir</p>
    <h1 style="margin:0">
      <span class="title-script">Gather</span>
      <span class="title-joiner">the</span>
      <span class="title-main">MARROW</span>
    </h1>
    <p class="author" style="margin:0">Delia<br>Marsh</p>
  </main>
</body>
</html>
```